Business Card Design

We need a business card for our café and health food store
We are called Mossy Lantern café and Health Foods, so all I have used for a logo so far is a couple of black foot prints under our name.
About 6 foot prints. We are also located by the beach so I thought that maybe some foot prints on the beach which would somehow also represent healthy food and our casual café.
We are open seven days a week and our colour tone is sort of terracotta, sort of Earthy look. We do good coffee and good food for breakfast, lunch and dinner. We are also open seven days for breakfast and lunch, dinner only 3 nights a week.

Industry/Entity Type

Health

Contact Information for Business Card

Mossy Lantern Café and Health Foods
27 Wattlebrook Lane
Fernhollow
Victoria 3871
Phone 03 5981 4072
ABN 58 276 914 803

```html
<!DOCTYPE html>
<html lang="en">
<head>
<meta charset="utf-8">
<title>Mossy Lantern Café and Health Foods – Business Card</title>
<link rel="stylesheet" href="https://fonts.googleapis.com/css2?family=Cutive+Mono&family=Kaushan+Script&display=swap">
<style>
  :root {
    --backdrop: #e4e4e4;
    --sand-light: #d8cda6;
    --sand: #cbbd8f;
    --sand-deep: #b9aa7b;
    --ink: #3a352c;
    --terracotta: #c2372a;
    --mark-tone: #a89a6e;
  }
  html, body {
    margin: 0;
    padding: 0;
    width: 1200px;
    height: 750px;
    overflow: hidden;
    background: var(--backdrop);
  }
  .stage {
    position: relative;
    width: 1200px;
    height: 750px;
  }
  .business-card {
    position: absolute;
    left: 150px;
    top: 125px;
    width: 900px;
    height: 500px;
    border-radius: 38px;
    background: radial-gradient(ellipse at 40% 40%, var(--sand-light), var(--sand) 60%, var(--sand-deep));
    box-shadow: 0 6px 18px rgba(0,0,0,0.18);
    color: var(--ink);
    font-family: "Cutive Mono", "Courier New", monospace;
  }
  .business-name {
    position: absolute;
    left: 44px;
    top: 135px;
    margin: 0;
    font-weight: 400;
    font-size: 34px;
    line-height: 40px;
    letter-spacing: 0.5px;
  }
  .business-name span { display: block; }
  .business-name .joiner { padding-left: 110px; }
  .business-name .second-line { padding-left: 80px; }
  .footprint-mark {
    position: absolute;
    left: 200px;
    top: 270px;
    width: 170px;
    height: 180px;
    border-radius: 16px;
    background: linear-gradient(160deg, var(--sand-deep), var(--mark-tone));
    opacity: 0.55;
  }
  .contact {
    position: absolute;
    left: 488px;
    top: 62px;
    font-size: 25px;
    line-height: 32px;
    font-style: normal;
  }
  .contact-row {
    position: relative;
    padding-left: 34px;
  }
  .contact-row .icon {
    position: absolute;
    left: 0;
    top: 5px;
    width: 24px;
    height: 24px;
  }
  .address-line.indented { padding-left: 110px; }
  .phone-row { margin-top: 20px; padding-left: 120px; }
  .phone-row .icon { left: 86px; }
  .opening-hours {
    position: absolute;
    right: 50px;
    top: 336px;
    margin: 0;
    font-family: "Kaushan Script", cursive;
    font-size: 24px;
    color: var(--terracotta);
  }
  .abn {
    position: absolute;
    right: 50px;
    top: 392px;
    margin: 0;
    font-size: 22px;
  }
  .abn .label { color: var(--terracotta); }
</style>
</head>
<body>
<main class="stage">
  <section class="business-card">
    <h1 class="business-name">
      <span>Mossy Lantern Café</span>
      <span class="joiner">and</span>
      <span class="second-line">Health Foods</span>
    </h1>
    <div class="footprint-mark" role="img" aria-label="Logo mark: a trail of six footprints in the sand"></div>

    <address class="contact">
      <div class="contact-row">
        <svg class="icon" viewBox="0 0 24 24" aria-hidden="true">
          <circle cx="12" cy="12" r="10" fill="none" stroke="var(--terracotta)" stroke-width="2"/>
          <path d="M12 6.5a3.5 3.5 0 0 0-3.5 3.5c0 2.6 3.5 6.5 3.5 6.5s3.5-3.9 3.5-6.5A3.5 3.5 0 0 0 12 6.5z" fill="var(--terracotta)"/>
          <circle cx="12" cy="10" r="1.3" fill="var(--sand)"/>
        </svg>
        <div class="address-line">27 Wattlebrook Lane</div>
        <div class="address-line indented">Fernhollow</div>
        <div class="address-line indented">Victoria 3871</div>
      </div>
      <div class="contact-row phone-row">
        <svg class="icon" viewBox="0 0 24 24" aria-hidden="true">
          <path d="M6.6 3.5l2.6 3.3-1.6 2.1c1 2.2 2.9 4.2 5.3 5.4l2.1-1.6 3.3 2.6-1.6 3.2c-6.8-.4-12.3-5.9-12.7-12.7z" fill="none" stroke="var(--terracotta)" stroke-width="2" stroke-linejoin="round"/>
        </svg>
        03 5981 4072
      </div>
    </address>

    <p class="opening-hours">We are open seven days a week.</p>
    <p class="abn"><span class="label">ABN</span> 58 276 914 803</p>
  </section>
</main>
</body>
</html>
```